This is for a poster that will be hanging in the window of a Men's Suit Store in the mall:
Size 4 feet wide by 6 feet high
Main point is: A sale on "Suits" or "Men's Suits" at 40%-60% off ( the 40%-60% off should be the focal point)
Some words that can be used are "Sale" or "Clearance Sale"
Some key words that can be used to make it urgent are "limited time offer" or something similar.
You can get creative, the point is for the customer to want to come into the store and buy a suit right away.
You may use a graphic (picture of a man in a suit). It is not necessary but if it looks good you can use it. (If you do use a picture, it should be of a modern fit or slim fit suit)
Sorry, the initial brief somehow got deleted from the project. Please see the updated brief.
Thanks
Reason: Project was closed for some reason, extended to give enough time to complete
Target Market(s)
Mostly Men ages 35-55
Industry/Entity Type
Store
Colors
Designer to choose colors to be used in the design.

```html
<!DOCTYPE html>
<html lang="en">
<head>
<meta charset="utf-8">
<title>Suit Sale Window Poster</title>
<link rel="stylesheet" href="https://fonts.googleapis.com/css2?family=Arimo:wght@700&display=swap">
<style>
  :root {
    --poster-black: #231f20;
    --sale-orange: #f26522;
    --text-white: #ffffff;
  }
  html, body {
    margin: 0;
    padding: 0;
    width: 800px;
    height: 1200px;
    overflow: hidden;
    background: var(--poster-black);
  }
  .poster {
    display: block;
    width: 800px;
    height: 1200px;
  }
  .poster-bg { fill: var(--poster-black); }
  .offer-panel { fill: var(--sale-orange); }
  .poster-text {
    fill: var(--text-white);
    font-family: "Arimo", "Helvetica Neue", Arial, sans-serif;
    font-weight: 700;
  }
</style>
</head>
<body>
<svg class="poster" viewBox="0 0 800 1200" xmlns="http://www.w3.org/2000/svg" role="img" aria-label="Suit yourself! 40% to 60% off mens suits, limited time only!">
  <rect class="poster-bg" x="0" y="0" width="800" height="1200"/>

  <text class="poster-text headline" x="69" y="86" font-size="90" textLength="662" lengthAdjust="spacingAndGlyphs">suit yourself!</text>

  <rect class="offer-panel" x="32" y="117" width="736" height="939"/>

  <g class="discount-range">
    <text class="poster-text discount-number" x="60" y="400" font-size="344" textLength="420" lengthAdjust="spacingAndGlyphs">40</text>
    <text class="poster-text discount-percent" x="482" y="392" font-size="250" textLength="222" lengthAdjust="spacingAndGlyphs">%</text>
    <text class="poster-text discount-joiner" x="544" y="512" font-size="136" textLength="100" lengthAdjust="spacingAndGlyphs">to</text>
    <text class="poster-text discount-number" x="60" y="816" font-size="344" textLength="420" lengthAdjust="spacingAndGlyphs">60</text>
    <text class="poster-text discount-percent" x="482" y="776" font-size="250" textLength="222" lengthAdjust="spacingAndGlyphs">%</text>
    <text class="poster-text discount-off" x="528" y="872" font-size="118" textLength="208" lengthAdjust="spacingAndGlyphs">OFF</text>
  </g>

  <text class="poster-text product-line" x="64" y="1008" font-size="144" textLength="676" lengthAdjust="spacingAndGlyphs">MENS SUITS</text>

  <text class="poster-text urgency-line" x="69" y="1146" font-size="90" textLength="662" lengthAdjust="spacingAndGlyphs">limited time only!</text>
</svg>
</body>
</html>
```